Talented energy healer needs business card design

I need a business card design for a new energy healing business in Perth Australia. As an energy healer I am quite earthy and practical rather than floaty and fairydust.
One of the techniques I use is unique in Australia but used internationally (US, UK and Europe). I practice with Coastal Pathway Therapy, Reiki and massage as well as some other techniques I developed personally. I am starting to incorporate sound healing into my practice. I literally change people's lives. The potential for each client is wide open. A key skill I bring to my practice is the capacity for making difficult situations seem more fun and less stressful.
Clients are likely to be depressed, physically unwell, going through a difficult time, unhappy with their current situation. They are people looking for new options to solve a difficult existing problem. They have probably tried other avenues before they come to me. They are open to something different.

I would like to communicate that the client and I work together for their healing and personal growth. I would like to convey that while the work of changing is challenging it can also be fun.

Hi all, info required on the card is:

Name
Title: Healer
contact number (mobile)
I don''t have a logo - I would be interested in seeing designs that use the whole card as well as the traditional logo on one side / in one corner. Whatever ''look/feel'' I choose will carry over to the website as well.

thanks
Meg

Reason: One or two of the designs caught my eye and many appeal for different reasons, but nothing is quite right for me. I've invited a couple of other designers to contribute so I wanted to give them time to be involved. kind regards Meg

Thank you all for the fabulous designs. I really appreciated the thought that many people put into my brief and a number of designs captured important things about what I was trying to say. It was a hard choice between 3 designs in the end.
thanks again and kind regards
Meg

Target Market(s)

people looking for new options to solve a difficult existing problem

Industry/Entity Type

Massage

Logo styles of interest
Abstract Logo
Requirements
Must have
• include green and blue
Nice to have
• hands, tea / teapots , the ocean, stepping stones

```html
<!DOCTYPE html>
<html lang="en">
<head>
<meta charset="utf-8">
<title>Meg Whatever – Healer business card</title>
<link href="https://fonts.googleapis.com/css2?family=Alegreya+Sans:wght@500;700&family=Open+Sans:wght@300&display=swap" rel="stylesheet">
<style>
  :root {
    --page-bg: #eceae6;
    --sky-light: #f2f8f9;
    --sky-mid: #cfe4ea;
    --sea-light: #a9cfdc;
    --sea-mid: #7fb3c6;
    --sea-deep: #5a93aa;
    --teal: #13958a;
    --outline-white: #ffffff;
  }
  * { margin: 0; padding: 0; box-sizing: border-box; }
  html, body {
    width: 1200px;
    height: 800px;
    overflow: hidden;
    background: var(--page-bg);
  }
  .canvas {
    position: relative;
    width: 1200px;
    height: 800px;
    display: flex;
    align-items: center;
    justify-content: center;
  }
  .business-card {
    position: relative;
    width: 1050px;
    height: 600px;
    overflow: hidden;
    box-shadow: 0 10px 30px rgba(0,0,0,0.18);
  }
  .card-backdrop {
    position: absolute;
    inset: 0;
    width: 100%;
    height: 100%;
  }
  .card-name {
    position: absolute;
    left: 48px;
    top: 246px;
    font-family: "Alegreya Sans", sans-serif;
    font-weight: 700;
    font-size: 96px;
    line-height: 1;
    color: var(--teal);
    letter-spacing: 0.5px;
    white-space: nowrap;
  }
  .card-title {
    position: absolute;
    left: 770px;
    top: 188px;
    font-family: "Alegreya Sans", sans-serif;
    font-weight: 700;
    font-size: 34px;
    line-height: 1;
    color: var(--teal);
    white-space: nowrap;
  }
  .card-title .divider {
    font-weight: 500;
    margin-right: 8px;
  }
  .card-phone {
    position: absolute;
    left: 40px;
    bottom: 32px;
    font-family: "Open Sans", sans-serif;
    font-weight: 300;
    font-size: 120px;
    line-height: 1;
    letter-spacing: 2px;
    color: transparent;
    -webkit-text-stroke: 2px var(--outline-white);
    white-space: nowrap;
  }
</style>
</head>
<body>
  <main class="canvas">
    <article class="business-card">
      <svg class="card-backdrop" viewBox="0 0 1050 600" preserveAspectRatio="none" role="img" aria-label="Photograph of smooth stepping stones in calm, misty sea water under a pale sky">
        <defs>
          <linearGradient id="sea-sky" x1="0" y1="0" x2="0" y2="1">
            <stop offset="0" stop-color="var(--sky-light)"/>
            <stop offset="0.3" stop-color="var(--sky-mid)"/>
            <stop offset="0.45" stop-color="var(--sea-light)"/>
            <stop offset="0.75" stop-color="var(--sea-mid)"/>
            <stop offset="1" stop-color="var(--sea-deep)"/>
          </linearGradient>
        </defs>
        <rect x="0" y="0" width="1050" height="600" fill="url(#sea-sky)"/>
      </svg>
      <h1 class="card-name">Meg Whatever</h1>
      <p class="card-title"><span class="divider">|</span>Healer</p>
      <p class="card-phone">+0 987 654 3210</p>
    </article>
  </main>
</body>
</html>
```